Broschüre für Sprachschule für die Vorstellung der Leistungen
Zielgruppe
Es geht um eine Broschüre einer Sprachschule für die Vorstellung der Leistungen:
Sprachkurse: A1, A2, B1. B2, C1, Fachsprache Ärzte, Fachspräche Pflegepersonal, Fachsprache Ingenieure
Seminare: Businessplan für Migranten, Unternehmensführung für Migranten, Ausbildung zur Pflegefachkraft, Existenzgründung für Migranten
Aufgabenstellung
Es handelt sich um ein Sprachschule/Bildungszentrum. Farben: Royal Blau, Gold

```html
<!DOCTYPE html>
<html lang="de">
<head>
<meta charset="utf-8">
<title>Sprachkurse &amp; Seminare – Broschüre</title>
<link rel="stylesheet" href="https://fonts.googleapis.com/css2?family=Open+Sans:wght@400;600;700&display=swap">
<style>
:root{
  --royal:#232a78;
  --gold:#b49c5c;
  --sand:#d3c395;
  --paper:#ffffff;
  --bg:#e4e4e4;
  --ink-light:#ffffff;
}
*{margin:0;padding:0;box-sizing:border-box}
html,body{width:1200px;height:1000px;overflow:hidden;background:var(--bg);font-family:"Open Sans",Arial,sans-serif}
.canvas{position:relative;width:1200px;height:1000px}
.page{position:absolute;background:var(--paper);overflow:hidden}
.abs{position:absolute}
.photo{position:absolute}
.blue{background:var(--royal);color:var(--ink-light)}
.gold{background:var(--gold);color:var(--ink-light)}
.sand{background:var(--sand)}
.logo-box{position:absolute;background:var(--paper);color:var(--royal);font-size:21px;font-weight:400;display:flex;align-items:center;justify-content:center;letter-spacing:.5px}
.logo-plain{position:absolute;color:var(--royal);font-size:21px;font-weight:400;letter-spacing:.5px}
.heading{font-size:9.5px;text-transform:uppercase;line-height:1.25;font-weight:400}
.body-text{font-size:6.6px;line-height:1.3}
.body-text p{margin-top:6px}
.body-text ul{list-style:none;margin-top:6px}
.body-text li{padding-left:7px;position:relative;margin-top:5px}
.body-text li::before{content:"•";position:absolute;left:0}
.on-white{color:var(--royal)}
.spine{position:absolute;top:0;bottom:0;width:14px;background:linear-gradient(90deg,rgba(0,0,0,0),rgba(0,0,0,.12),rgba(0,0,0,0))}
.level{font-size:46px;font-weight:700;line-height:1}
.small-caps{font-size:9px;font-weight:700;text-transform:uppercase}
.schedule{font-size:6.6px;line-height:1.6;text-transform:uppercase}
</style>
</head>
<body>
<div class="canvas">

  <!-- Front cover -->
  <section class="page cover" style="left:135px;top:70px;width:294px;height:412px">
    <div class="photo" role="img" aria-label="Foto: drei Lernende arbeiten gemeinsam am Tisch mit Notizen" style="left:10px;top:8px;width:284px;height:265px;background:linear-gradient(135deg,#c9b8a2,#8e7d6a 55%,#d7d2c8)"></div>
    <div class="logo-box" style="left:178px;top:8px;width:95px;height:43px">LOGO</div>
    <div class="abs blue" style="left:0;top:273px;width:294px;height:139px"></div>
    <div class="abs gold" style="left:0;top:241px;width:222px;height:65px;padding:12px 0 0 19px;font-size:19px;line-height:1.08;font-weight:400">SPRACHKURSE<br>&amp; SEMINARE</div>
    <p class="abs" style="left:20px;top:323px;width:260px;color:#fff;font-size:9.6px;line-height:1.27">berum secto quibus cum se parum volupta temperum fugia natus vero ma voluptatisi sequamusam rerchilli-quo ea diaerum, iur</p>
  </section>

  <!-- Inner spread: introduction -->
  <section class="page spread" style="left:462px;top:70px;width:571px;height:412px">
    <div class="logo-plain" style="left:32px;top:40px">LOGO</div>
    <div class="photo" role="img" aria-label="Foto: lächelnde Kursteilnehmerin mit Büchern im Flur" style="left:126px;top:8px;width:226px;height:267px;background:linear-gradient(160deg,#b7b2a6,#6f6a5f 50%,#9aa092)"></div>
    <div class="abs sand" style="left:0;top:248px;width:397px;height:164px"></div>
    <div class="abs blue" style="left:31px;top:165px;width:159px;height:247px;padding:10px 9px">
      <h2 class="heading">Imilis maione cusam quibus pelesto</h2>
      <div class="body-text">
        <p>volorem consequ ibustia volenis et occum untusam, omniet verrum iliciliqui ut aut lame aut eos iliquunt estem. Officipsam il endi conseque experios sequi blaborit excepudae prae estrunt odicil ipis vollaut plabor sim repe num, voluptatis dolo vit,</p>
        <p>suntis dem liquiat ecerrov itibus ad et et harcit autem con et doluptatasi te seribus, cor aliqui nossent estrum solore mo quia quam volor aut et elibus eiur, seque ilis erae occabor eicatem non preium volesti onsequi</p>
        <p>berum secto quibus cum se parum volupta temperum fugia natus vero ma voluptatisi sequamusam rerchilliquo ea diaerum, iur</p>
      </div>
    </div>
    <div class="abs blue" style="left:304px;top:0;width:236px;height:332px;padding:64px 20px 0 79px">
      <h2 class="heading">Imilis maione cusam<br>quibus pelesto</h2>
      <div class="body-text">
        <p>volorem consequ ibustia volenis et occum untusam, omniet verrum iliciliqui ut aut lame aut eos iliquunt estem. Officipsam il endi conseque experios sequi blaborit excepudae prae estrunt odicil ipis vollaut plabor sim repe num, voluptatis dolo vit,</p>
        <p>suntis dem liquiat ecerrov itibus ad et et harcit autem con et doluptatasi te seribus, cor aliqui nossent estrum solore mo quia quam volor aut et elibus eiur, seque ilis erae occabor eicatem non preium volesti onsequi</p>
        <p>berum secto quibus cum se parum volupta temperum fugia natus vero ma voluptatisi sequamusam rerchilliquo ea diaerum, iur</p>
        <p>volorem consequ ibustia volenis et occum untusam, omniet verrum iliciliqui ut aut lame aut eos iliquunt estem. Officipsam il endi conseque experios sequi blaborit excepudae prae estrunt odicil ipis vollaut plabor sim repe num, voluptatis dolo vit,</p>
      </div>
    </div>
    <div class="abs on-white" style="left:408px;top:350px">
      <h3 class="small-caps">Kontakt</h3>
      <p class="body-text" style="margin-top:8px">Musterstraße 1, 12345 Musterstadt<br>Tel. 01234 567890, www.Website.de</p>
    </div>
    <div class="spine" style="left:278px"></div>
  </section>

  <!-- Inner spread: B1 / B2 -->
  <section class="page spread" style="left:137px;top:518px;width:571px;height:414px">
    <div class="abs blue" style="left:2px;top:83px;width:94px;height:331px">
      <div class="level" style="position:absolute;left:22px;top:18px">B1</div>
      <div style="position:absolute;right:13px;bottom:14px;text-align:right">
        <h3 class="small-caps">Kurszeiten</h3>
        <p class="schedule" style="margin-top:6px">12 Einheiten<br>Di 19-20 Uhr<br>Mi 19-20 Uhr</p>
      </div>
    </div>
    <div class="abs sand" style="left:96px;top:167px;width:190px;height:55px"></div>
    <div class="photo" role="img" aria-label="Foto: Teilnehmerin arbeitet konzentriert am Laptop" style="left:97px;top:223px;width:160px;height:169px;background:linear-gradient(180deg,#f2f2f0,#dcd9d4 60%,#8b8580)"></div>
    <div class="abs on-white" style="left:125px;top:28px;width:140px">
      <h2 class="heading">Imilis maione cusam<br>quibus pelesto</h2>
      <div class="body-text">
        <p>volorem consequ ibustia volenis et occum untusam, omniet verrum iliciliqui ut aut lame aut eos iliquunt estem. Officipsam il endi conseque experios sequi</p>
        <p>blaborit excepudae prae estrunt odicil ipis vollaut plabor sim repe num, volupta-tis dolo vit,</p>
        <ul>
          <li>suntis dem liquiat ecerrov itibus ad et et harcit autem con et doluptatasi te seribus,</li>
          <li>cor aliqui nossent estrum solore mo quia quam volor aut et elibus eiur,</li>
          <li>seque ilis erae occabor eicatem non preium volesti onsequi</li>
        </ul>
      </div>
    </div>

    <div class="abs sand" style="left:314px;top:0;width:160px;height:82px"></div>
    <div class="abs blue" style="left:474px;top:0;width:95px;height:330px">
      <div style="position:absolute;left:15px;top:24px">
        <h3 class="small-caps">Kurszeiten</h3>
        <p class="schedule" style="margin-top:4px">12 Einheiten<br>Mo 19-20 Uhr<br>Do 19-20 Uhr</p>
      </div>
      <div class="level" style="position:absolute;left:20px;bottom:12px;color:#e6e6ec">B2</div>
    </div>
    <div class="abs on-white" style="left:314px;top:114px;width:140px">
      <h2 class="heading">Imilis maione cusam<br>quibus pelesto</h2>
      <div class="body-text">
        <p>volorem consequ ibustia volenis et occum untusam, omniet verrum iliciliqui ut aut lame aut eos iliquunt estem. Officipsam il endi conseque experios sequi</p>
        <p>blaborit excepudae prae estrunt odicil ipis vollaut plabor sim repe num, volupta-tis dolo vit,</p>
        <ul>
          <li>suntis dem liquiat ecerrov itibus ad et et harcit autem con et doluptatasi te seribus,</li>
          <li>cor aliqui nossent estrum solore mo quia quam volor aut et elibus eiur,</li>
          <li>seque ilis erae occabor eicatem non preium volesti onsequi</li>
        </ul>
        <p>berum secto quibus cum se parum volupta temperum fugia natus vero ma voluptatisi sequamusam rerchilliquo ea diaerum, iur</p>
        <p>volorem consequ ibustia volenis et occum untusam, omniet verrum iliciliqui ut aut lame aut eos iliquunt estem. Officipsam il endi conseque experios sequi blaborit excepudae prae estrunt odicil ipis vollaut plabor sim repe num, voluptatis dolo vit,</p>
      </div>
    </div>
    <div class="spine" style="left:278px"></div>
  </section>

  <!-- Back cover -->
  <section class="page back-cover" style="left:749px;top:518px;width:288px;height:412px">
    <div class="photo" role="img" aria-label="Foto: Gruppe von Lernenden lacht gemeinsam am Tisch mit Laptop" style="left:9px;top:8px;width:279px;height:267px;background:linear-gradient(135deg,#d8d1c4,#8d7a67 50%,#bfc3c6)"></div>
    <div class="abs blue" style="left:0;top:275px;width:288px;height:137px"></div>
    <div class="logo-box" style="left:29px;top:275px;width:86px;height:42px">LOGO</div>
    <div class="abs gold" style="left:125px;top:332px;width:134px;height:80px;text-align:center;padding-top:9px">
      <h3 class="small-caps" style="font-weight:600">Kontakt</h3>
      <p class="body-text" style="margin-top:8px;color:#ece3c8">Musterstraße 1<br>12345 Musterstadt</p>
      <p class="body-text" style="margin-top:6px;color:#ece3c8">Tel. 01234 567890<br>www.Website.de</p>
    </div>
  </section>

</div>
</body>
</html>
```